Melissa Dorvan Personal Business Card

I like orange. It's would better if my card have an orange background
Address: 5820 Halvers Lane #417
San Jose
California
US
Tel: 4085172049

Industry/Entity Type

Business

```html
<!DOCTYPE html>
<html lang="en">
<head>
<meta charset="utf-8">
<title>Melissa Dorvan – Business Card</title>
<link rel="stylesheet" href="https://fonts.googleapis.com/css2?family=Oleo+Script:wght@700&family=Pathway+Gothic+One&display=swap">
<style>
  :root {
    --paper: #ffffff;
    --sun-yellow: #fcf762;
    --salmon: #eb8870;
    --sky-blue: #57bbec;
    --lime: #9fce19;
    --tangerine: #e8852d;
    --name-fill: #ea7a1c;
    --ink: #1a120c;
    --contact-ink: #2a1a10;
  }
  html, body {
    margin: 0;
    padding: 0;
    overflow: hidden;
    background: var(--paper);
  }
  .card {
    position: relative;
    width: 1200px;
    height: 688px;
    background: var(--paper);
    overflow: hidden;
  }
  .block {
    position: absolute;
  }
  .block--name {
    left: 7px; top: 7px; width: 860px; height: 275px;
    background: var(--sun-yellow);
  }
  .block--salmon {
    left: 898px; top: 3px; width: 299px; height: 452px;
    background: var(--salmon);
  }
  .block--sky {
    left: 2px; top: 311px; width: 430px; height: 373px;
    background: var(--sky-blue);
  }
  .block--lime {
    left: 461px; top: 311px; width: 406px; height: 143px;
    background: var(--lime);
  }
  .block--contact {
    left: 457px; top: 481px; width: 739px; height: 203px;
    background: var(--tangerine);
  }
  .name {
    position: absolute;
    left: 48px;
    top: 78px;
    width: 790px;
    margin: 0;
    font-family: "Oleo Script", cursive;
    font-weight: 700;
    font-size: 104px;
    line-height: 1;
    letter-spacing: 3px;
    color: var(--name-fill);
    -webkit-text-stroke: 2.5px var(--ink);
    transform: skewX(-8deg);
    white-space: nowrap;
  }
  .contact {
    position: absolute;
    right: 56px;
    top: 520px;
    margin: 0;
    font-family: "Pathway Gothic One", "Arial Narrow", sans-serif;
    font-style: normal;
    font-size: 33px;
    line-height: 40px;
    text-align: right;
    color: var(--contact-ink);
  }
  .contact span {
    display: block;
  }
</style>
</head>
<body>
  <main class="card">
    <div class="block block--name"></div>
    <div class="block block--salmon"></div>
    <div class="block block--sky"></div>
    <div class="block block--lime"></div>
    <div class="block block--contact"></div>

    <h1 class="name">Melissa Dorvan</h1>

    <address class="contact">
      <span class="contact__street">5820 Halvers Lane #417</span>
      <span class="contact__city">San Jose, California U.S.A.</span>
      <span class="contact__phone">Tel: 4085172049</span>
    </address>
  </main>
</body>
</html>
```